tunWisp Pursuits - Cycling Headphones

Looking for a set of web banners for a product we're bringing to the Australian market:
tunWisp Pursuits are in-ear headphones designed to provide the wearer with total sound awareness; which obviously makes listening to music or podcasts a lot safer for cyclists.

You can get a full run down on the product over at http://www.tunWispPursuits.example.au

The banners will be tested across the web, and also provided to our affiliate partners to use in their promotions.

Tag Lines can include:
Cycle Safer
Total Sound awareness
Worlds Safest Headphones
Originally designed for NDQ + RVT
(or feel free to get creative)

Please also include a strong call to action button to elicit response. Something like [Order Today] [Find Our Mote] [Click Here To Cycle Safer] etc etc

Target Market(s)

Cyclists: Generally 30-55 years old.

Industry/Entity Type

Affiliate

Font styles to use
Serif
Sans Serif

Requirements
Must have
• Call to Action Button.
• Image of Cyclist and/or product
• Tagline of some description.

```html
<!DOCTYPE html>
<html lang="en">
<head>
<meta charset="utf-8">
<title>tunWisp Pursuits – Total Sound Awareness Banner</title>
<link rel="stylesheet" href="https://fonts.googleapis.com/css2?family=Quicksand:wght@400;500;700&display=swap">
<style>
  :root {
    --page-bg: #1b1b1b;
    --teal-light: #4fb8c0;
    --teal-mid: #329ea8;
    --teal-deep: #1f8590;
    --white: #ffffff;
    --ink: #0f2f33;
    --badge-orange: #e98a1e;
    --frame-dark: #111111;
    --skin-light: #d9b9a8;
    --skin-mid: #a88474;
    --hair-dark: #3a3430;
  }
  * { margin: 0; padding: 0; box-sizing: border-box; }
  html, body {
    width: 1200px; height: 900px; overflow: hidden;
    background: var(--page-bg);
    font-family: "Quicksand", sans-serif;
  }
  .banner {
    position: absolute; left: 32px; top: 231px;
    width: 1132px; height: 419px; overflow: hidden;
    background: radial-gradient(ellipse at 45% 35%, var(--teal-light) 0%, var(--teal-mid) 45%, var(--teal-deep) 100%);
    box-shadow: 0 6px 12px rgba(0,0,0,0.6);
  }
  .banner-decor { position: absolute; inset: 0; }
  .product-photo {
    position: absolute; left: 0; top: 55px; width: 320px; height: 320px;
    background: radial-gradient(ellipse at 25% 40%, var(--skin-light) 0%, rgba(217,185,168,0.35) 40%, rgba(79,184,192,0) 70%);
  }
  .ear-photo {
    position: absolute; left: 788px; top: 36px; width: 346px; height: 346px;
    border: 3px solid var(--frame-dark);
    background: linear-gradient(160deg, var(--hair-dark) 0%, #6e5a50 35%, var(--skin-light) 60%, var(--skin-mid) 100%);
  }
  .headline {
    position: absolute; right: 362px; top: 58px;
    text-align: right; color: var(--white);
  }
  .headline-title { font-size: 41px; font-weight: 700; letter-spacing: 1px; line-height: 1; }
  .headline-sub { font-size: 15px; font-weight: 700; letter-spacing: 1px; margin-top: 4px; }
  .tagline {
    position: absolute; left: 268px; top: 178px;
    color: var(--white); font-size: 34px; font-weight: 400; letter-spacing: 1.5px;
    padding-bottom: 2px; border-bottom: 3px solid var(--white); line-height: 1.1;
  }
  .cta-button {
    position: absolute; left: 349px; top: 301px; width: 159px; height: 34px;
    display: flex; align-items: center; justify-content: center;
    background: linear-gradient(var(--teal-light), var(--teal-mid));
    border: 2px solid var(--white); border-radius: 8px;
    color: var(--ink); font-size: 19px; font-weight: 500; letter-spacing: 1px;
    box-shadow: 0 6px 10px rgba(0,0,0,0.35);
    text-decoration: none;
  }
  .offer-badge { position: absolute; left: 0; top: 0; width: 76px; height: 76px; }
</style>
</head>
<body>
  <section class="banner">
    <svg class="banner-decor" width="1132" height="419" viewBox="0 0 1132 419">
      <polygon points="0,419 1132,80 1132,160 0,419" fill="rgba(255,255,255,0.06)"/>
      <circle cx="668" cy="21" r="28" fill="rgba(255,255,255,0.12)"/>
      <circle cx="620" cy="248" r="42" fill="rgba(255,255,255,0.12)"/>
      <circle cx="283" cy="360" r="42" fill="rgba(255,255,255,0.12)"/>
      <circle cx="220" cy="100" r="68" fill="rgba(255,255,255,0.08)"/>
      <circle cx="20" cy="410" r="32" fill="rgba(255,255,255,0.1)"/>
      <polygon points="565,419 595,419 820,190 820,160" fill="rgba(255,255,255,0.3)"/>
      <polygon points="655,419 690,419 820,290 820,255" fill="rgba(255,255,255,0.3)"/>
      <polygon points="945,36 975,36 1010,0 980,0" fill="rgba(255,255,255,0.3)"/>
      <polygon points="1040,36 1075,36 1110,0 1075,0" fill="rgba(255,255,255,0.3)"/>
    </svg>

    <div class="product-photo" role="img" aria-label="Hand holding the clear in-ear headphone with its thin ear hook"></div>

    <div class="headline">
      <h1 class="headline-title">TOTAL SOUND AWARENESS</h1>
      <p class="headline-sub">WORLD SAFEST HEADPHONES</p>
    </div>

    <p class="tagline">WE WANT YOU TO RIDE SAFE</p>

    <a class="cta-button" href="http://www.tunWispPursuits.example.au">ORDER NOW</a>

    <div class="ear-photo" role="img" aria-label="Side view of a rider's ear wearing the headphone behind the ear"></div>

    <svg class="offer-badge" viewBox="0 0 76 76">
      <polygon points="0,0 76,0 0,76" fill="var(--badge-orange)"/>
      <text x="23" y="29" transform="rotate(-45 23 29)" text-anchor="middle" font-family="Quicksand, sans-serif" font-weight="700" font-size="12" fill="#111">50%</text>
      <text x="30" y="38" transform="rotate(-45 30 38)" text-anchor="middle" font-family="Quicksand, sans-serif" font-weight="700" font-size="12" fill="#111">OFF</text>
    </svg>
  </section>
</body>
</html>
```